CONTACT US Page and design for website

We need a contact us page for our website. We would like it to have a message area, a map, our information, etc.

Please see the text attachment for what we are looking for. We need to have something that is creative and interesting, modern and professional.

We believe that a contact US page should be very creative because everyone clicks that to contact us. We want it to be super professional, attention grabbing, pleasing to the eye.

PLEASE KEEP THE HEADER AND FOOTER THE SAME, ONLY THE ACTUAL CONTACT US PAGE NEEDS TO BE WORKED ON. THANKS!
We are excited to work with designers for this project.

Target Market(s)

Clients in technology business

Industry/Entity Type

Information Technology

Number of Pages Required

1 page

Font styles to use
Serif

Requirements
Must have
• CHECK THE TEXT ATTACHMENT PLEASE
• Must stay within our design colors and theme.
Nice to have
• see attachment
Should not have
• it should be special

```html
<!DOCTYPE html>
<html lang="en">
<head>
<meta charset="utf-8">
<title>Contact — Norvane Systems</title>
<link rel="stylesheet" href="https://fonts.googleapis.com/css2?family=Oswald:wght@300;400&family=PT+Sans:wght@400&display=swap">
<style>
  :root {
    --teal: #2aa5a1;
    --teal-deep: #1b7c79;
    --ink: #111111;
    --text: #2b2b2b;
    --placeholder: #9a9a9a;
    --field-top: #ffffff;
    --field-bottom: #e9e9e9;
    --field-line: #dddddd;
    --map-base: #e6e6e4;
    --white: #ffffff;
  }
  * { box-sizing: border-box; margin: 0; padding: 0; }
  html, body { width: 1200px; height: 691px; overflow: hidden; background: var(--white); }
  body { position: relative; font-family: "PT Sans", sans-serif; color: var(--text); }

  .connect-bar {
    position: absolute; left: 0; top: 25px; width: 1200px; height: 66px;
    background: var(--teal);
  }
  .connect-bar__lead {
    position: absolute; left: 0; top: 0; width: 399px; height: 66px;
    background: linear-gradient(90deg, var(--teal-deep) 0%, var(--teal) 100%);
    clip-path: polygon(0 0, 380px 0, 399px 33px, 380px 66px, 0 66px);
  }
  .connect-bar__chevron { position: absolute; left: 378px; top: 0; }
  .connect-bar__title {
    position: absolute; left: 169px; top: 11px;
    font-family: "Oswald", sans-serif; font-weight: 300; font-size: 33px; line-height: 40px;
    color: var(--white); letter-spacing: 0;
  }
  .social { position: absolute; top: 37px; width: 42px; height: 42px; border: 2px solid var(--white); border-radius: 50%;
    display: flex; align-items: center; justify-content: center;
    font-family: "PT Sans", sans-serif; font-size: 11px; color: var(--white); }
  .social--feed { left: 436px; }
  .social--post { left: 522px; }
  .social--pics { left: 603px; }
  .social--work { left: 684px; }

  .page-title {
    position: absolute; left: 0; width: 1272px; top: 112px; text-align: center;
    font-family: "Oswald", sans-serif; font-weight: 400; font-size: 55px; line-height: 68px;
    color: var(--ink); letter-spacing: -1px;
  }

  .field {
    position: absolute; left: 155px; width: 474px;
    background: linear-gradient(180deg, var(--field-top) 0%, var(--field-bottom) 100%);
    border: 1px solid var(--field-line);
    font-size: 12px; color: var(--placeholder); padding-left: 22px;
  }
  .field--name { top: 206px; height: 43px; line-height: 41px; }
  .field--email { top: 267px; height: 43px; line-height: 41px; }
  .field--subject { top: 328px; height: 43px; line-height: 41px; }
  .field--message { top: 387px; height: 131px; padding-top: 14px; }

  .location-map {
    position: absolute; left: 702px; top: 206px; width: 357px; height: 316px;
    background: var(--map-base); border: 1px solid var(--field-line);
  }

  .send-button {
    position: absolute; left: 155px; top: 544px; width: 177px; height: 52px;
    background: linear-gradient(180deg, var(--teal) 0%, var(--teal-deep) 100%);
    color: var(--white); font-family: "PT Sans", sans-serif; font-size: 30px; line-height: 52px;
    text-align: center; letter-spacing: 1px;
  }

  .contact-item { position: absolute; top: 562px; height: 22px; display: flex; align-items: center; gap: 12px; font-size: 12px; color: var(--text); }
  .contact-item--mail { left: 372px; }
  .contact-item--phone { left: 580px; gap: 13px; }
  .contact-item--place { left: 765px; gap: 14px; }

  .site-footer {
    position: absolute; left: 0; top: 630px; width: 1200px; height: 45px;
    background: var(--teal); color: var(--white); font-size: 12px; line-height: 45px;
  }
  .site-footer__copy { position: absolute; left: 155px; }
  .site-footer__links { position: absolute; right: 142px; }
</style>
</head>
<body>
  <header class="connect-bar">
    <div class="connect-bar__lead"></div>
    <svg class="connect-bar__chevron" width="24" height="66" viewBox="0 0 24 66">
      <polyline points="2,0 21,33 2,66" fill="none" stroke="#16625f" stroke-width="3"/>
    </svg>
    <div class="connect-bar__title">Connect with us</div>
  </header>
  <span class="social social--feed">Feed</span>
  <span class="social social--post">Post</span>
  <span class="social social--pics">Pics</span>
  <span class="social social--work">Work</span>

  <h1 class="page-title">GET IN TOUCH</h1>

  <div class="field field--name">Name</div>
  <div class="field field--email">Email</div>
  <div class="field field--subject">Subject</div>
  <div class="field field--message">Message</div>

  <div class="location-map" role="img" aria-label="Street map showing the office location at 418 Halden Ave, Westbrook"></div>

  <div class="send-button">SEND</div>

  <div class="contact-item contact-item--mail">
    <svg width="27" height="18" viewBox="0 0 27 18"><rect x="1" y="1" width="25" height="16" fill="none" stroke="#222" stroke-width="1.5"/><polyline points="1,1 13.5,10 26,1" fill="none" stroke="#222" stroke-width="1.5"/><line x1="1" y1="17" x2="10" y2="8" stroke="#222" stroke-width="1.5"/><line x1="26" y1="17" x2="17" y2="8" stroke="#222" stroke-width="1.5"/></svg>
    <span>hello@norvanesys.com</span>
  </div>
  <div class="contact-item contact-item--phone">
    <svg width="25" height="25" viewBox="0 0 25 25"><circle cx="12.5" cy="12.5" r="11.3" fill="none" stroke="#222" stroke-width="1.5"/><path d="M9 6.5 L11 10 L9.6 11.6 Q11 14.4 13.4 15.6 L15 14 L18.5 16 L17 18.5 Q12 19 8.5 13 Q6.8 9 9 6.5 Z" fill="none" stroke="#222" stroke-width="1.4" stroke-linejoin="round"/></svg>
    <span>555-014-2270</span>
  </div>
  <div class="contact-item contact-item--place">
    <svg width="20" height="28" viewBox="0 0 20 28"><path d="M10 27 C4 18 1.5 13.5 1.5 9.5 A8.5 8.5 0 0 1 18.5 9.5 C18.5 13.5 16 18 10 27 Z" fill="none" stroke="#222" stroke-width="1.6"/><circle cx="10" cy="9.5" r="3.2" fill="none" stroke="#222" stroke-width="1.6"/></svg>
    <span>Norvane Systems, 418 Halden Ave. Westbrook, CA 90417</span>
  </div>

  <footer class="site-footer">
    <span class="site-footer__copy">Norvane Systems, LLC. Copyright © 2017</span>
    <span class="site-footer__links">Terms of Services | Privacy Policy &nbsp;| Sitemap</span>
  </footer>
</body>
</html>
```